Vesk Architecture

We are a architectural design and build company working between scales 1/1000 to 1/1 we want people to understand our difference from our design experience and quality.we build hotels restourants and office spaces.Our company name is Vesk architecture to mind sustainability.

We want to write our adress phone and work spesifications on the card and we want our logo as backround.

Ps:you could find the logo adress and phone box numbers from the web:www.veskmimarlik-ornek.com

Target Market(s)

Who looks for experts.

Industry/Entity Type

Architecture

Requirements
Must have
• Design is over everything.
Should not have
• we don want it to be colorfull

```html
<!DOCTYPE html>
<html lang="tr">
<head>
<meta charset="utf-8">
<title>Vesk Mimarlık – Business Card</title>
<link rel="stylesheet" href="https://fonts.googleapis.com/css2?family=Roboto+Condensed:wght@300;400;700&display=swap">
<style>
  :root {
    --page: #ffffff;
    --frame: #d6d6d6;
    --card: #55412c;
    --card-edge: #3f2f1f;
    --glow: rgba(255, 255, 255, 0.22);
    --ink: #ffffff;
    --ink-soft: #e6ddd2;
    --ink-muted: #c9b9a6;
  }
  html, body {
    margin: 0;
    padding: 0;
    width: 1200px;
    height: 945px;
    overflow: hidden;
    background: var(--page);
  }
  .sheet {
    position: relative;
    width: 1200px;
    height: 945px;
    box-sizing: border-box;
    border: 2px solid var(--frame);
    background: var(--page);
    font-family: "Roboto Condensed", "Arial Narrow", sans-serif;
  }
  .card {
    position: absolute;
    left: 334px;
    width: 510px;
    height: 292px;
    border-radius: 28px;
    background: var(--card);
    border: 1px solid var(--card-edge);
    box-shadow: 0 1px 3px rgba(0, 0, 0, 0.25);
    overflow: hidden;
    color: var(--ink);
  }
  .card--front {
    top: 160px;
    background: radial-gradient(circle at 50% 38%, rgba(255,255,255,0.2) 0, rgba(255,255,255,0.06) 90px, rgba(255,255,255,0) 170px), var(--card);
  }
  .card--back {
    top: 503px;
    background: radial-gradient(circle at 10% 6%, rgba(255,255,255,0.28) 0, rgba(255,255,255,0.08) 60px, rgba(255,255,255,0) 150px), var(--card);
  }
  .front-name {
    position: absolute;
    left: 0;
    right: 0;
    top: 92px;
    text-align: center;
    font-weight: 300;
    font-size: 92px;
    line-height: 92px;
    letter-spacing: 2px;
    color: var(--ink);
  }
  .brand {
    position: absolute;
    left: 34px;
    top: 84px;
    font-weight: 300;
    color: var(--ink);
  }
  .brand__word {
    display: block;
    font-size: 84px;
    line-height: 84px;
    letter-spacing: 1px;
  }
  .brand__sub {
    display: block;
    margin-top: 10px;
    font-size: 17px;
    letter-spacing: 2.5px;
  }
  .divider {
    position: absolute;
    left: 226px;
    top: 36px;
    width: 2px;
    height: 222px;
    background: var(--ink);
  }
  .contact {
    position: absolute;
    left: 243px;
    top: 74px;
    font-size: 13.5px;
    line-height: 18px;
    color: var(--ink-soft);
  }
  .contact p { margin: 0; }
  .contact__name { margin-bottom: 12px !important; }
  .contact__address { margin-bottom: 14px !important; }
  .contact__phone { font-weight: 700; color: var(--ink); font-size: 12.5px; line-height: 19px; }
  .contact__mail { margin-top: 12px !important; color: var(--ink-muted); }
  .contact__mail b { color: var(--ink); font-weight: 700; }
</style>
</head>
<body>
  <main class="sheet">
    <section class="card card--front" aria-label="Card front">
      <div class="front-name">vesk</div>
    </section>

    <section class="card card--back" aria-label="Card back">
      <div class="brand">
        <span class="brand__word">vesk</span>
        <span class="brand__sub">MİMARLIK</span>
      </div>
      <div class="divider"></div>
      <div class="contact">
        <p class="contact__name">Deniz Arda KAYA - Mimar</p>
        <p class="contact__address">Sakin Mah. Ilgın Cad. Yaprak Sok.<br>No : 7 Kadıköy / ISTANBUL</p>
        <p class="contact__phone">t. 0216 555 01 42<br>f. 0216 555 01 43</p>
        <p class="contact__mail"><b>e.</b> studio@veskmimarlik-ornek.com</p>
      </div>
    </section>
  </main>
</body>
</html>
```